Very high end short term vacation rentals.

Amber Tide Harbor Estates. Design business cards using existing logo. Should represent high quality, class accommodations. The back side will have a QR code linking to website/video and pictures

```html
<!DOCTYPE html>
<html lang="en">
<head>
<meta charset="utf-8">
<title>Amber Tide Harbor Estates – Business Cards</title>
<link rel="stylesheet" href="https://fonts.googleapis.com/css2?family=Poppins:wght@400;700&display=swap">
<style>
  :root {
    --page-bg: #ffffff;
    --card-front-top: #fdf1f3;
    --card-front-bottom: #fbe5f2;
    --card-back: #000000;
    --ink: #111111;
    --ink-light: #ffffff;
    --accent-gold: #f2c200;
    --divider: #8a8a8a;
    --logo-ghost: #2b2b2b;
    --shadow: rgba(0, 0, 0, 0.45);
  }
  * { margin: 0; padding: 0; box-sizing: border-box; }
  html, body {
    width: 800px; height: 1200px; overflow: hidden;
    background: var(--page-bg);
    font-family: "Poppins", sans-serif;
  }
  .canvas { position: relative; width: 800px; height: 1200px; }
  .card {
    position: absolute; left: 100px; width: 600px; height: 343px;
    overflow: hidden;
    box-shadow: 0 8px 14px var(--shadow);
  }
  .card--front {
    top: 222px;
    background: linear-gradient(160deg, var(--card-front-top) 0%, var(--card-front-bottom) 100%);
  }
  .card--back { top: 610px; background: var(--card-back); }

  .front-waves { position: absolute; inset: 0; width: 100%; height: 100%; }

  .seahorse-art {
    position: absolute; left: 55px; top: 62px; width: 98px; height: 217px;
    background: linear-gradient(180deg, #9a9a9e 0%, #5c5c66 55%, #c9c6cc 100%);
    border-radius: 40px 40px 50px 20px;
    opacity: 0.75;
  }
  .divider {
    position: absolute; left: 185px; top: 92px; width: 1px; height: 171px;
    background: var(--divider);
  }
  .owner-name {
    position: absolute; left: 243px; top: 86px;
    font-size: 18px; font-weight: 700; color: var(--ink); letter-spacing: 0.3px;
  }
  .hummingbird-art {
    position: absolute; border-radius: 50%;
    background: radial-gradient(circle at 40% 50%, #f4e04a 0%, #ee5fae 50%, #9fc7ea 85%, transparent 100%);
  }
  .hummingbird-art--front { left: 452px; top: 16px; width: 128px; height: 129px; opacity: 0.85; }
  .hummingbird-art--back { left: 272px; top: 46px; width: 104px; height: 104px; opacity: 0.9; }

  .contact-list { position: absolute; left: 216px; top: 196px; list-style: none; }
  .contact-item {
    display: flex; align-items: center; gap: 9px;
    height: 23.5px; font-size: 14.5px; color: var(--ink);
  }
  .contact-item svg { width: 16px; height: 16px; flex: none; }
  .contact-item--extra { position: absolute; left: 326px; top: 273px; }

  .brand-ghost {
    position: absolute; left: 21px; top: 40px; width: 170px;
    font-size: 26px; font-weight: 700; line-height: 1.25;
    color: var(--logo-ghost);
  }
  .back-web {
    position: absolute; left: 245px; top: 292px;
    display: flex; align-items: center; gap: 9px;
    font-size: 14.5px; color: var(--ink-light);
  }
  .back-web svg { width: 17px; height: 17px; }
</style>
</head>
<body>
<main class="canvas">

  <section class="card card--front" aria-label="Business card front">
    <svg class="front-waves" viewBox="0 0 600 343" preserveAspectRatio="none" aria-hidden="true">
      <path d="M0 255 C180 250 360 200 600 95" fill="none" stroke="#ffffff" stroke-width="1.5" opacity="0.8"/>
      <path d="M0 280 C200 270 380 215 600 120" fill="none" stroke="#ffffff" stroke-width="1" opacity="0.7"/>
      <path d="M60 343 C260 300 420 240 600 170" fill="none" stroke="#ffffff" stroke-width="1" opacity="0.6"/>
    </svg>

    <div class="seahorse-art" role="img" aria-label="Pencil illustration of a seahorse"></div>
    <div class="divider"></div>
    <h1 class="owner-name">Owner Name</h1>
    <div class="hummingbird-art hummingbird-art--front" role="img" aria-label="Watercolour illustration of a hummingbird in flight"></div>

    <ul class="contact-list">
      <li class="contact-item">
        <svg viewBox="0 0 24 24" fill="none" stroke="var(--accent-gold)" stroke-width="1.6"><path d="M5 3h4l2 5-3 2a12 12 0 0 0 6 6l2-3 5 2v4a2 2 0 0 1-2 2A17 17 0 0 1 3 5a2 2 0 0 1 2-2z"/></svg>
        <span>555 014 2290</span>
      </li>
      <li class="contact-item">
        <svg viewBox="0 0 24 24" fill="none" stroke="var(--accent-gold)" stroke-width="1.6"><rect x="2" y="5" width="20" height="14"/><path d="M2 5l10 8 10-8"/></svg>
        <span>stay@ambertideharbor.net</span>
      </li>
      <li class="contact-item">
        <svg viewBox="0 0 24 24" fill="none" stroke="var(--accent-gold)" stroke-width="1.6"><circle cx="12" cy="12" r="10"/><ellipse cx="12" cy="12" rx="4.5" ry="10"/><path d="M2 12h20M4 7h16M4 17h16"/></svg>
        <span>www.ambertideharbor.net</span>
      </li>
    </ul>
    <div class="contact-item contact-item--extra">
      <svg viewBox="0 0 24 24" fill="none" stroke="var(--accent-gold)" stroke-width="1.6"><circle cx="12" cy="12" r="10"/><ellipse cx="12" cy="12" rx="4.5" ry="10"/><path d="M2 12h20M4 7h16M4 17h16"/></svg>
      <span>www.ambertideharbor.net</span>
    </div>
  </section>

  <section class="card card--back" aria-label="Business card back">
    <p class="brand-ghost">Amber Tide Harbor Estates</p>
    <div class="hummingbird-art hummingbird-art--back" role="img" aria-label="Watercolour illustration of a hummingbird in flight"></div>
    <div class="back-web">
      <svg viewBox="0 0 24 24" fill="none" stroke="var(--accent-gold)" stroke-width="1.6"><circle cx="12" cy="12" r="10"/><ellipse cx="12" cy="12" rx="4.5" ry="10"/><path d="M2 12h20M4 7h16M4 17h16"/></svg>
      <span>www.ambertideharbor.net</span>
    </div>
  </section>

</main>
</body>
</html>
```